Professional DJ Business Card

Business card for giving out to clubs and venues or interested groups that are in need of a professional DJ. I want something artistic and catchy/alluring, with a minimalist approach that gets just the vital amount of info and leaves the rest for inquiry via contacting me. Ideally I would like one side to have an image of something cool like an eye and my name, then the other side be the contact info, I am definitely feeling a black or dark colored card, but I am open to other designs. I am uploading a picture that I made that reflects a little of what I am *kind of* looking for.

Industry/Entity Type

Business

Contact Information for Business Card

Tomas Velander (Kalvo)
Professional DJ (West Coast)
EDM (Deep/House/Techno), Hip Hop, Latin, Trap.
Cell: 555-274-8391
Email: Kalvoofficial@mailbrook.net
www.tunevault.net/oxfernwaits

```html
<!DOCTYPE html>
<html lang="en">
<head>
<meta charset="utf-8">
<title>Kalvo – DJ Business Card</title>
<link rel="stylesheet" href="https://fonts.googleapis.com/css2?family=Arimo:wght@400;700&display=swap">
<style>
  :root{
    --page:#e9e7e3;
    --front-card:#c9c9c9;
    --back-card:#131614;
    --back-card-edge:#202421;
    --ink-light:#ffffff;
    --ink-soft:#d9dcda;
    --mark-dark:#ffffff;
  }
  *{margin:0;padding:0;box-sizing:border-box}
  html,body{width:1200px;height:950px;overflow:hidden}
  body{
    background:var(--page);
    font-family:"Arimo", Arial, sans-serif;
    position:relative;
  }
  .card{
    position:absolute;
    left:240px;
    width:720px;
    height:411px;
    border-radius:4px;
    box-shadow:0 8px 24px rgba(0,0,0,.25);
    overflow:hidden;
  }
  .card--front{
    top:48px;
    background:linear-gradient(135deg,#d4d4d4 0%,var(--front-card) 60%,#bdbdbd 100%);
    display:flex;align-items:center;justify-content:center;
  }
  .card--back{
    top:491px;
    background:linear-gradient(135deg,var(--back-card) 0%,var(--back-card-edge) 55%,var(--back-card) 100%);
    color:var(--ink-light);
  }
  .card--back::after{
    content:"";position:absolute;inset:0;
    background:linear-gradient(115deg,transparent 55%,rgba(255,255,255,.06) 56%,rgba(255,255,255,.02) 80%,transparent 81%);
    pointer-events:none;
  }
  .brand{
    display:flex;align-items:center;gap:14px;
    color:var(--mark-dark);
    font-weight:700;
  }
  .brand__dot{
    width:22px;height:22px;border-radius:50%;
    background:currentColor;
  }
  .card--front .brand{font-size:64px;letter-spacing:2px}
  .card--front .brand__dot{width:30px;height:30px}
  .back__brand{
    position:absolute;left:52px;top:70px;
    font-size:44px;letter-spacing:1px;
  }
  .back__info{
    position:absolute;left:52px;top:196px;
    font-size:15px;line-height:1.45;color:var(--ink-soft);
  }
  .genres{margin-bottom:10px}
  .contact{list-style:none}
  .contact li{display:flex;align-items:center;gap:10px;height:22px}
  .contact svg{width:14px;height:14px;flex:none;fill:none;stroke:var(--ink-soft);stroke-width:1.6}
  .identity{
    position:absolute;right:56px;top:168px;
    text-align:left;
  }
  .identity__name{font-size:19px;font-weight:700;color:var(--ink-light)}
  .identity__role{font-size:15px;color:var(--ink-soft);margin-top:4px}
</style>
</head>
<body>

<section class="card card--front" aria-label="Card front">
  <div class="brand"><span class="brand__dot"></span><span class="brand__name">Kalvo</span></div>
</section>

<section class="card card--back" aria-label="Card back">
  <div class="brand back__brand"><span class="brand__dot"></span><span class="brand__name">Kalvo</span></div>

  <div class="back__info">
    <p class="genres">EDM (Deep/House/Techno)<br>Hip Hop, Latin, Trap.</p>
    <ul class="contact">
      <li>
        <svg viewBox="0 0 14 14" aria-hidden="true"><rect x="3.5" y="1" width="7" height="12" rx="1.2"/><line x1="6" y1="11" x2="8" y2="11"/></svg>
        <span>555-274-8391</span>
      </li>
      <li>
        <svg viewBox="0 0 14 14" aria-hidden="true"><rect x="1" y="3" width="12" height="8"/><polyline points="1,3 7,8 13,3"/></svg>
        <span>Kalvoofficial@mailbrook.net</span>
      </li>
      <li>
        <svg viewBox="0 0 14 14" aria-hidden="true"><circle cx="7" cy="7" r="5.5"/><line x1="1.5" y1="7" x2="12.5" y2="7"/></svg>
        <span>oxfernwaits</span>
      </li>
    </ul>
  </div>

  <div class="identity">
    <p class="identity__name">Tomas Velander (Kalvo)</p>
    <p class="identity__role">Professional DJ (West Coast)</p>
  </div>
</section>

</body>
</html>
```